Facebook Ads for Leading Telemedicine Provider

Need a variation of this advertisement.

Would like to leave everything the same with white as the dominant color but test the pink circle with a different design style

Target Market(s)

Male / Female from 18-65

Industry/Entity Type

Health

Requirements
Must have
• Use the image attached and test a different background

```html
<!DOCTYPE html>
<html lang="en">
<head>
<meta charset="UTF-8">
<title>Vitalo – Free Covid Testing at Home</title>
<link href="https://fonts.googleapis.com/css2?family=Source+Sans+3:wght@600;700&display=swap" rel="stylesheet">
<style>
  :root {
    --page-white: #ffffff;
    --teal-deep: #0b4f5c;
    --teal-mid: #0f8a86;
    --teal-light: #3fc7a8;
    --mint-glow: #8fe6c4;
    --navy: #0e1a6b;
    --text-white: #ffffff;
    --scene-gold: #e2b43a;
    --scene-cream: #fbf1d2;
    --scene-olive: #8a7a3c;
    --plant-green: #4f9a5a;
    --plant-pot: #4a5a78;
  }
  * { margin: 0; padding: 0; box-sizing: border-box; }
  html, body {
    width: 1200px;
    height: 1200px;
    overflow: hidden;
    background: var(--page-white);
  }
  .ad-canvas {
    position: relative;
    width: 1200px;
    height: 1200px;
    overflow: hidden;
    background: var(--page-white);
    font-family: "Source Sans 3", "Myriad Pro", Arial, sans-serif;
  }
  .hero-circle {
    position: absolute;
    left: -176px;
    top: -117px;
    width: 1242px;
    height: 1242px;
    border-radius: 50%;
    background:
      radial-gradient(circle at 36% 57%, rgba(143, 230, 196, 0.55) 0%, rgba(63, 199, 168, 0.35) 22%, rgba(15, 138, 134, 0) 40%),
      radial-gradient(circle at 70% 30%, var(--teal-light) 0%, var(--teal-mid) 35%, var(--teal-deep) 80%);
  }
  .brand-name {
    position: absolute;
    left: 143px;
    top: 82px;
    font-size: 68px;
    font-weight: 700;
    color: var(--text-white);
    letter-spacing: 0.5px;
    line-height: 1;
  }
  .headline {
    position: absolute;
    left: 108px;
    top: 318px;
    font-size: 132px;
    font-weight: 600;
    line-height: 140px;
    color: var(--text-white);
    letter-spacing: -1px;
  }
  .book-button {
    position: absolute;
    left: 180px;
    top: 792px;
    width: 434px;
    height: 103px;
    background: var(--navy);
    border-radius: 6px;
    display: flex;
    align-items: center;
    justify-content: center;
    color: var(--text-white);
    font-size: 44px;
    font-weight: 700;
    letter-spacing: 0.5px;
  }
  .scene-doorway {
    position: absolute;
    left: 700px;
    top: 595px;
    width: 265px;
    height: 500px;
    border-radius: 14px;
    background: linear-gradient(170deg, var(--scene-cream) 0%, var(--scene-gold) 60%, var(--scene-olive) 100%);
  }
  .scene-plant {
    position: absolute;
    left: 622px;
    top: 950px;
    width: 128px;
    height: 200px;
    border-radius: 60px 60px 18px 18px;
    background: linear-gradient(180deg, var(--plant-green) 0%, var(--plant-green) 60%, var(--plant-pot) 100%);
  }
  .scene-worker {
    position: absolute;
    left: 1005px;
    top: 540px;
    width: 170px;
    height: 560px;
    border-radius: 40px 40px 14px 14px;
    background: linear-gradient(180deg, #c9d3df 0%, var(--scene-gold) 35%, var(--scene-olive) 100%);
  }
  .site-url {
    position: absolute;
    left: 176px;
    top: 1158px;
    font-size: 35px;
    font-weight: 600;
    color: var(--navy);
    line-height: 1;
  }
</style>
</head>
<body>
  <main class="ad-canvas">
    <div class="hero-circle" role="img" aria-label="Teal backdrop of floating virus particles seen through a large magnifying glass"></div>

    <div class="brand-name">Vitalo</div>

    <h1 class="headline">Free Covid<br>Testing at<br>Home</h1>

    <div class="book-button">BOOK NOW</div>

    <div class="scene-plant" role="img" aria-label="Illustration of a potted green plant beside the front door"></div>
    <div class="scene-doorway" role="img" aria-label="Illustration of a woman opening her front door above a welcome mat"></div>
    <div class="scene-worker" role="img" aria-label="Illustration of a health worker with a clipboard, below a crossed-out virus icon and a shield tick badge"></div>

    <div class="site-url">https://vitalo.org/covid-testing</div>
  </main>
</body>
</html>
```